Cardiology practice business card

We need a business card for our cardiology practice "Bellmoor Cardiology". We have a new logo, attached below. We like the colours in the logo - red and charcoal. The front of the business card will need to have the doctors name, address, phone number and email. The back will need to have space to write 2 appointment dates and times.

```html
<!DOCTYPE html>
<html lang="en">
<head>
<meta charset="utf-8">
<title>Bellmoor Cardiology – Business Card</title>
<link href="https://fonts.googleapis.com/css2?family=Lato:wght@300;400;700;900&display=swap" rel="stylesheet">
<style>
  :root {
    --red: #d7141f;
    --charcoal-dark: #232427;
    --charcoal-light: #7a7b7e;
    --ink: #2a2a2a;
    --white: #ffffff;
    --page: #e6e6e6;
    --dots: #555555;
  }
  * { box-sizing: border-box; margin: 0; padding: 0; }
  html, body {
    width: 1200px; height: 1122px; overflow: hidden;
    background: var(--page);
    font-family: "Lato", sans-serif;
  }
  .card {
    position: absolute;
    left: 250px;
    width: 700px; height: 400px;
    border-radius: 22px;
    overflow: hidden;
    box-shadow: 0 6px 18px rgba(0,0,0,0.18);
  }

  /* Back: appointment card */
  .card--back { top: 90px; background: var(--white); }
  .appointment__title {
    position: absolute; top: 30px; left: 0; right: 0;
    text-align: center; color: var(--red);
    font-weight: 900; font-size: 38px; letter-spacing: 0.5px; line-height: 1.1;
  }
  .field {
    position: absolute; display: flex; align-items: flex-end;
    color: var(--red); font-size: 17px; text-transform: uppercase; line-height: 1.2;
  }
  .field__line {
    flex: 1; border-bottom: 2px dotted var(--dots);
    margin: 0 4px 4px;
  }
  .field--name { top: 98px; left: 60px; width: 580px; }
  .field--date { left: 60px; width: 340px; }
  .field--time { left: 405px; width: 235px; }
  .row-1 { top: 138px; }
  .row-2 { top: 178px; }
  .days {
    position: absolute; top: 232px; left: 60px; width: 580px;
    display: flex; justify-content: space-between; list-style: none;
  }
  .days__item {
    display: flex; align-items: center; gap: 8px;
    font-size: 18px; color: var(--ink);
  }
  .days__box {
    width: 17px; height: 17px; border: 2.5px solid var(--red);
  }
  .appointment__note {
    position: absolute; top: 290px; left: 60px; width: 580px;
    font-size: 16px; line-height: 1.45; color: var(--ink);
  }

  /* Front: contact card */
  .card--front {
    top: 620px;
    background: linear-gradient(160deg, var(--charcoal-dark) 20%, var(--charcoal-light) 100%);
  }
  .front__panel { position: absolute; inset: 0; }
  .person { position: absolute; top: 44px; left: 44px; }
  .person__name {
    color: var(--red); font-weight: 900; font-size: 34px;
    text-transform: uppercase; letter-spacing: 0.5px;
  }
  .person__title { color: #e8e8e8; font-size: 20px; font-weight: 400; margin-top: 4px; }
  .contact {
    position: absolute; left: 44px; top: 210px; list-style: none;
    color: var(--white); font-size: 17px; line-height: 1.35;
  }
  .contact__item { display: flex; align-items: flex-start; gap: 10px; margin-bottom: 6px; }
  .contact__icon { width: 16px; height: 16px; flex: none; margin-top: 3px; fill: var(--red); }
  .brand {
    position: absolute; left: 420px; top: 160px; width: 250px;
    text-align: center; color: var(--red);
    font-weight: 900; font-size: 30px; line-height: 1.15;
    text-transform: uppercase; letter-spacing: 1px;
  }
</style>
</head>
<body>

<section class="card card--back" aria-label="Appointment card">
  <h2 class="appointment__title">NEXT APPOINTMENT</h2>
  <div class="field field--name">Name<span class="field__line"></span></div>
  <div class="field field--date row-1">Date<span class="field__line"></span></div>
  <div class="field field--time row-1">Time<span class="field__line"></span>AM\PM</div>
  <div class="field field--date row-2">Date<span class="field__line"></span></div>
  <div class="field field--time row-2">Time<span class="field__line"></span>AM\PM</div>
  <ul class="days">
    <li class="days__item"><span class="days__box"></span>MON</li>
    <li class="days__item"><span class="days__box"></span>TUES</li>
    <li class="days__item"><span class="days__box"></span>WED</li>
    <li class="days__item"><span class="days__box"></span>THU</li>
    <li class="days__item"><span class="days__box"></span>FRI</li>
    <li class="days__item"><span class="days__box"></span>SAT</li>
  </ul>
  <p class="appointment__note">If you are unable to keep your appointment, please call us to reschedule at least 48 hours prior to your appointment.</p>
</section>

<section class="card card--front" aria-label="Contact card">
  <svg class="front__panel" viewBox="0 0 700 400" preserveAspectRatio="none" aria-hidden="true">
    <path d="M700 0 L500 0 C 360 90, 340 300, 440 400 L700 400 Z" fill="#ffffff"/>
  </svg>
  <div class="person">
    <h1 class="person__name">Daniel Hartley</h1>
    <p class="person__title">Cardiologist &amp; CEO</p>
  </div>
  <ul class="contact">
    <li class="contact__item">
      <svg class="contact__icon" viewBox="0 0 16 16"><path d="M8 0a5.5 5.5 0 0 0-5.5 5.5C2.5 10 8 16 8 16s5.5-6 5.5-10.5A5.5 5.5 0 0 0 8 0zm0 8a2.5 2.5 0 1 1 0-5 2.5 2.5 0 0 1 0 5z"/></svg>
      <span>423 Street Address Here, City<br>State &amp; Country, ZIP Code</span>
    </li>
    <li class="contact__item">
      <svg class="contact__icon" viewBox="0 0 16 16"><path d="M3.6 1 6 3.8 4.6 5.6a9 9 0 0 0 5.8 5.8L12.2 10l2.8 2.4-1.6 2.6C7 15 1 9 1 2.6z"/></svg>
      <span>(123) 456-7890</span>
    </li>
    <li class="contact__item">
      <svg class="contact__icon" viewBox="0 0 16 16"><path d="M1 3h14v10H1zm1.5 1.2L8 8.6l5.5-4.4z" fill-rule="evenodd"/></svg>
      <span>info@yourwebsitehere.com</span>
    </li>
    <li class="contact__item">
      <svg class="contact__icon" viewBox="0 0 16 16"><circle cx="8" cy="8" r="7"/><path d="M1 8h14M8 1c-3 3.5-3 10.5 0 14M8 1c3 3.5 3 10.5 0 14" stroke="#232427" stroke-width="1" fill="none"/></svg>
      <span>yourwebsitehere.com</span>
    </li>
  </ul>
  <p class="brand">Bellmoor<br>Cardiology</p>
</section>

</body>
</html>
```